Mediation service showing compassion, collaboration, and resolution

I would like to purchase a customized version of a design you have previously submitted - https://www.brieflyart.example/design/48172036

Hello,

I would like a design for a flyer for my mediation business.
I also want to include a message that says that I offer rates on sliding scale.
My website is: www.morvenpeaceadr.example

Let me know what other details you might want?

Thank you,

Tobias

Target Market(s)

Local community, western Massachusetts USA. Businesses, families, individuals.

Industry/Entity Type

Mediation, Legal, Alternative Dispute Resolution, Divorce, Unions

Font styles to use
Sans Serif

Colors
0094D4
00A9DD
6FCCEA
C7EBF8
E9F6FB
00AB8E
00BBA5
67D7C9
C6EFE9
E9F9F6

Requirements
Must have
• “Sliding scale rates available “. Phone and email details. +1.555.784.3091 and email: tobias@morvenpeaceadr.example as well as we code to my website www.morvenpeaceadr.example

```html
<!DOCTYPE html>
<html lang="en">
<head>
<meta charset="utf-8">
<title>Need a Mediator? – Tobias F. Morvenpeace ADR</title>
<link rel="stylesheet" href="https://fonts.googleapis.com/css2?family=Montserrat:ital,wght@1,800&family=Mulish:wght@300;400;500;600;700;800&display=swap">
<style>
  :root {
    --navy: #121f44;
    --orange: #f0982a;
    --white: #ffffff;
    --ink: #111111;
    --teal: #67d7c9;
    --sky: #6fccea;
    --row: rgba(96, 124, 176, 0.62);
    --row-line: rgba(200, 212, 235, 0.75);
  }
  * { box-sizing: border-box; margin: 0; padding: 0; }
  html, body { width: 927px; height: 1200px; overflow: hidden; background: var(--white); }
  body { font-family: "Mulish", Arial, sans-serif; }

  .flyer { position: relative; width: 927px; height: 1200px; background: var(--white); overflow: hidden; }

  .brand { position: absolute; left: 59px; top: 66px; width: 280px; text-align: center; color: var(--ink); }
  .brand__name { font-size: 25px; font-weight: 500; letter-spacing: 0.2px; white-space: nowrap; }
  .brand__tag { margin-top: 10px; font-size: 8.5px; font-weight: 700; letter-spacing: 0.3px; }

  .headline { position: absolute; left: 56px; top: 207px; color: var(--navy); font-family: "Montserrat", Arial, sans-serif;
    font-weight: 800; font-style: italic; font-size: 71px; line-height: 68px; letter-spacing: -1px; }
  .tagline { position: absolute; left: 60px; top: 350px; color: var(--orange); font-size: 28px;
    font-weight: 700; letter-spacing: 0.3px; }

  .band { position: absolute; left: 0; top: 419px; width: 927px; height: 126px; background: var(--navy); }
  .backdrop { position: absolute; left: 0; top: 555px; width: 927px; height: 645px;
    background: radial-gradient(ellipse at 30% 35%, #4c6699 0%, #2a4273 40%, #14244a 75%, #0c1530 100%); }

  .portrait { position: absolute; left: 563px; top: 59px; width: 305px; height: 381px;
    background: linear-gradient(180deg, #8d959b 0%, #9a8f88 45%, #c2555e 75%, #b84753 100%); }

  .services { position: absolute; left: 59px; top: 486px; width: 395px; }
  .services__title { height: 94px; background: var(--orange); color: var(--white); font-size: 30px;
    font-weight: 800; display: flex; align-items: center; justify-content: center; letter-spacing: 0.3px; }
  .services__list { list-style: none; background: var(--row); }
  .services__item { height: 65px; display: flex; align-items: center; border-bottom: 1.5px solid var(--row-line);
    color: var(--white); font-size: 17.5px; font-weight: 500; line-height: 21px; letter-spacing: 0.3px;
    padding-left: 23px; white-space: nowrap; }
  .services__item:last-child { border-bottom: none; height: 63px; }
  .services__tick { width: 34px; height: 30px; flex: none; margin-right: 18px; }

  .about { position: absolute; left: 532px; top: 613px; width: 336px; color: var(--white); }
  .about__title { font-size: 26px; font-weight: 300; letter-spacing: 0.5px; margin-left: 35px; margin-bottom: 16px; }
  .about__text { font-size: 16px; font-weight: 400; line-height: 21.2px; letter-spacing: 0.45px; }
  .about__text strong { color: var(--orange); font-weight: 800; }

  .contact { position: absolute; left: 536px; top: 962px; width: 340px; color: var(--white); }
  .contact__row { display: flex; align-items: center; }
  .contact__row + .contact__row { margin-top: 10px; }
  .contact__icon { width: 42px; height: 42px; flex: none; margin-right: 22px; }
  .contact__label { font-size: 17px; font-weight: 400; letter-spacing: 0.4px; line-height: 18px; }
  .contact__phone { font-size: 26px; font-weight: 600; letter-spacing: 1px; line-height: 32px; }
  .contact__web { font-size: 15px; font-weight: 600; letter-spacing: 0.6px; white-space: nowrap; }
  .contact__email { margin: 12px 0 0 64px; font-size: 14px; font-weight: 500; letter-spacing: 0.3px; color: var(--sky); }
  .contact__rates { margin: 6px 0 0 64px; font-size: 14px; font-weight: 800; letter-spacing: 0.4px; color: var(--teal); }
</style>
</head>
<body>
<main class="flyer">
  <div class="band"></div>
  <div class="backdrop" role="img" aria-label="Dimmed blue photo of hands signing a document"></div>

  <header class="brand">
    <div class="brand__name">Tobias F. Morvenpeace</div>
    <div class="brand__tag">Alternative Dispute Resolution</div>
  </header>

  <h1 class="headline">NEED A<br>MEDIATOR?</h1>
  <p class="tagline">Manage and resolve conflict.</p>

  <div class="portrait" role="img" aria-label="Portrait photo of the mediator in a red shirt against grey siding"></div>

  <section class="services">
    <h2 class="services__title">SERVICES PROVIDED</h2>
    <ul class="services__list">
      <li class="services__item"><svg class="services__tick" viewBox="0 0 34 30"><path d="M2 17 L12 27 Q20 10 33 2 Q19 10 12 21 Z" fill="#f0982a"/></svg>Divorce and Family Mediation</li>
      <li class="services__item"><svg class="services__tick" viewBox="0 0 34 30"><path d="M2 17 L12 27 Q20 10 33 2 Q19 10 12 21 Z" fill="#f0982a"/></svg>Commercial and Business Mediation</li>
      <li class="services__item"><svg class="services__tick" viewBox="0 0 34 30"><path d="M2 17 L12 27 Q20 10 33 2 Q19 10 12 21 Z" fill="#f0982a"/></svg>International Business and Trading<br>Conflict Mediation</li>
      <li class="services__item"><svg class="services__tick" viewBox="0 0 34 30"><path d="M2 17 L12 27 Q20 10 33 2 Q19 10 12 21 Z" fill="#f0982a"/></svg>Merger Negotiations &amp; Business<br>Collaboration</li>
      <li class="services__item"><svg class="services__tick" viewBox="0 0 34 30"><path d="M2 17 L12 27 Q20 10 33 2 Q19 10 12 21 Z" fill="#f0982a"/></svg>Workplace Mediation</li>
      <li class="services__item"><svg class="services__tick" viewBox="0 0 34 30"><path d="M2 17 L12 27 Q20 10 33 2 Q19 10 12 21 Z" fill="#f0982a"/></svg>Mediation Coaching</li>
      <li class="services__item"><svg class="services__tick" viewBox="0 0 34 30"><path d="M2 17 L12 27 Q20 10 33 2 Q19 10 12 21 Z" fill="#f0982a"/></svg>Mediation via video conference</li>
      <li class="services__item"><svg class="services__tick" viewBox="0 0 34 30"><path d="M2 17 L12 27 Q20 10 33 2 Q19 10 12 21 Z" fill="#f0982a"/></svg>Ombuds contracting</li>
    </ul>
  </section>

  <section class="about">
    <h2 class="about__title">ABOUT TOBIAS</h2>
    <p class="about__text">Working in the international business world for <strong>over 30 years,</strong> Tobias has become very skilled in negotiation, mediation, and resolution of conflicts with his clients and suppliers. He also became adept at negotiating terms and relationships between companies and their representatives, as well as within companies. Over the course of his career, Tobias has had at least 400 employees reporting to him, and on many occasions, he acted as an ombudsman, helping to reach agreements between employees during times of conflict.</p>
  </section>

  <section class="contact">
    <div class="contact__row">
      <svg class="contact__icon" viewBox="0 0 42 42" fill="none" stroke="#fff" stroke-width="2.2">
        <circle cx="21" cy="21" r="19.5"/>
        <path d="M14 11 L17.5 10 L20 16 L17.5 18 Q19 23 24 25.5 L26 23 L32 25.5 L31 29 Q28 32 23 30 Q14 26 11 18 Q10 13 14 11 Z" stroke-linejoin="round"/>
      </svg>
      <div>
        <div class="contact__label">CALL TO FIND OUT MORE</div>
        <div class="contact__phone">+1.555.784.3091</div>
      </div>
    </div>
    <div class="contact__row">
      <svg class="contact__icon" viewBox="0 0 42 42" fill="none" stroke="#fff" stroke-width="2">
        <circle cx="20" cy="19" r="17"/>
        <ellipse cx="20" cy="19" rx="7.5" ry="17"/>
        <path d="M3 19 H37 M6 10 H34 M6 28 H26 M20 2 V36"/>
        <path d="M27 27 L39 32 L34 34 L37 39 L35 40 L32 35 L28 38 Z" fill="#fff"/>
      </svg>
      <div class="contact__web">WWW.MORVENPEACEADR.EXAMPLE</div>
    </div>
    <div class="contact__email">tobias@morvenpeaceadr.example</div>
    <div class="contact__rates">Sliding scale rates available</div>
  </section>
</main>
</body>
</html>
```